Label Design for Bra "Heron Lingerie" by Larkfield Apparel Company

The bra is packaged in a poly bag with a hanger. We require a label design for the brand name "Heron Lingerie" by Larkfield Apparel Company. The main label will be attached by a string on the bra. The size of that label will 25cm in length and 10cm wide. This is the first label the customer see's when she picks up the garment/bra. Therefore, we require an eye catching design for that. This classic full shape bra with smooth moulded double layered cups fit beautifully under t-shirts and fitted garments. The larkfield apparel company logo has been included and we would like it to feature in the label. A sample labels are also given.
Target Market(s)
Laddies 18 - 45
Industry/Entity Type
Clothing
Look and feel
Each slider illustrates characteristics of the customer's brand and the style your logo design should communicate.

```html
<!DOCTYPE html>
<html lang="en">
<head>
<meta charset="utf-8">
<title>Heron Lingerie – Label Options</title>
<link rel="stylesheet" href="https://fonts.googleapis.com/css2?family=Quicksand:wght@400;500;600&family=Open+Sans:ital,wght@0,700;1,700&display=swap">
<style>
  :root {
    --ink: #474356;
    --paper: #ffffff;
    --backdrop: #f4f4f5;
    --rose: #e0325f;
    --rose-soft: #e8628a;
    --mint: #b2d8c8;
  }
  * { box-sizing: border-box; margin: 0; padding: 0; }
  html, body { width: 1200px; height: 1000px; overflow: hidden; }
  body {
    background: var(--backdrop);
    font-family: "Quicksand", sans-serif;
    color: var(--ink);
    position: relative;
  }
  .label {
    position: absolute;
    top: 62px;
    width: 456px;
    height: 820px;
    background: var(--paper);
    box-shadow: 0 6px 30px rgba(0,0,0,0.12);
    overflow: hidden;
  }
  .label--one { left: 107px; }
  .label--two { left: 637px; }

  .maker {
    position: absolute;
    top: 212px;
    display: flex;
    align-items: center;
    gap: 8px;
    font-weight: 600;
    font-size: 15px;
    line-height: 1.2;
    color: var(--ink);
  }
  .maker__mark { width: 20px; height: 20px; background: var(--ink); flex: none; }
  .label--one .maker { left: 50px; }
  .label--two .maker { right: 45px; flex-direction: row-reverse; text-align: right; }

  .brand {
    position: absolute;
    top: 330px;
    font-weight: 500;
    font-size: 38px;
    line-height: 52px;
    letter-spacing: 0.5px;
    text-transform: uppercase;
  }
  .tagline {
    position: absolute;
    top: 462px;
    width: 200px;
    font-family: "Open Sans", sans-serif;
    font-style: italic;
    font-weight: 700;
    font-size: 13px;
    line-height: 19px;
  }
  .tagline__product { font-style: normal; font-size: 17px; }
  .copy {
    position: absolute;
    top: 555px;
    width: 190px;
    font-size: 12.5px;
    line-height: 17.5px;
    font-weight: 500;
  }
  .label--one .brand,
  .label--one .tagline,
  .label--one .copy { left: 48px; }
  .label--two .brand,
  .label--two .tagline,
  .label--two .copy { right: 45px; text-align: right; }
  .label--two .copy { width: 180px; }

  .band {
    position: absolute;
    left: 0;
    width: 100%;
    background: var(--ink);
    color: var(--paper);
    font-family: "Open Sans", sans-serif;
    font-size: 14px;
    line-height: 20px;
    font-weight: 400;
  }
  .band em { font-weight: 700; }
  .label--one .band { top: 726px; height: 94px; padding: 27px 0 0 48px; }
  .label--two .band { top: 728px; height: 52px; padding: 15px 0 0 38px; }

  .figure-art { position: absolute; }
  .figure-art--dressed {
    left: 263px; top: 168px; width: 193px; height: 652px;
    border-radius: 90px 0 0 0;
    background: linear-gradient(180deg, #f2f2f2 0%, #f2f2f2 18%, var(--rose) 32%, var(--rose-soft) 60%, var(--mint) 68%, var(--mint) 100%);
  }
  .figure-art--silhouette {
    left: 18px; top: 166px; width: 180px; height: 562px;
    border-radius: 80px 80px 10px 10px;
    background: var(--ink);
  }

  .caption {
    position: absolute;
    top: 902px;
    width: 456px;
    text-align: center;
    font-size: 36px;
    font-weight: 500;
    letter-spacing: 0.5px;
    color: var(--ink);
  }
  .caption--one { left: 107px; }
  .caption--two { left: 637px; }
</style>
</head>
<body>

  <section class="label label--one">
    <div class="figure-art figure-art--dressed" role="img" aria-label="Line illustration of a woman in a pink top and mint trousers, hand on hip"></div>
    <div class="maker"><span class="maker__mark"></span><span>Larkfield<br>apparel company</span></div>
    <h1 class="brand">Heron<br>Lingerie</h1>
    <p class="tagline">Classic Full Shape <span class="tagline__product">Bra</span> with Smooth Moulded Double Layered Cups</p>
    <p class="copy">Lorem ipsum dolor sit amet, consectetur adipisicing elit, sed do eiusmod tempor incididunt ut labore et dolore magna aliqua. Ut enim ad minim veniam, quis nostrud exercitation.</p>
    <div class="band"><em>Fits Beautifully</em> under<br>T-Shirts and Fitted Garments</div>
  </section>

  <section class="label label--two">
    <div class="figure-art figure-art--silhouette" role="img" aria-label="Dark silhouette of a woman posing in heels"></div>
    <div class="maker"><span class="maker__mark"></span><span>Larkfield<br>apparel company</span></div>
    <h1 class="brand">Heron<br>Lingerie</h1>
    <p class="tagline">Classic Full Shape <span class="tagline__product">Bra</span> with Smooth Moulded Double Layered Cups</p>
    <p class="copy">Lorem ipsum dolor sit amet, consectetur adipisicing elit, sed do eiusmod tempor incididunt ut labore et dolore magna aliqua. Ut enim ad minim veniam, quis nostrud exercitation.</p>
    <div class="band"><em>Fits Beautifully</em> under T-Shirts and Fitted Garments</div>
  </section>

  <p class="caption caption--one">OPTION 1</p>
  <p class="caption caption--two">OPTION 2</p>

</body>
</html>
```